Would like to get a new Ticket jacket or caddy design with a modern look for our travel company. Currently we use a one sided design. Photos attached. This ticket jacket will be used to put the domestic tickets for the resort islands and will be handed over to visitors. Free to use Maldives photos from http://bluelarkvoyage.example for ideas.

Reason: Please give 5 more days for selecting the best design and tweaking the final product

Target Market(s)

Travellers

Industry/Entity Type

Travel

Font styles to use
Sans Serif

Requirements
Must have
• Maldives photos, company addresses(Maldives and London)
Nice to have
• open to ideas
Should not have
• photos in photos or framed photos

```html
<!DOCTYPE html>
<html lang="en">
<head>
<meta charset="utf-8">
<title>Bluelark Voyage – Ticket Jacket</title>
<link rel="stylesheet" href="https://fonts.googleapis.com/css2?family=Arimo:wght@400;700&display=swap">
<style>
  :root {
    --bg: #c0c0c0;
    --black: #000000;
    --ink: #111111;
    --pink: #ff3d8b;
    --cyan: #5ff2f0;
    --green: #3fbf4a;
    --white: #ffffff;
    --sky-top: #2f86d8;
    --sky-mid: #8cc8ef;
    --sea: #1fa6e0;
    --sea-deep: #0a6fc0;
    --mark: #cfd3d8;
  }
  * { box-sizing: border-box; margin: 0; padding: 0; }
  html, body { width: 1200px; height: 1000px; overflow: hidden; }
  body { background: var(--bg); font-family: "Arimo", Arial, sans-serif; position: relative; }
  .abs { position: absolute; }

  .label { position: absolute; font-weight: 700; color: var(--black); line-height: 1; }
  .label--title { font-size: 66px; }
  .label--side { font-size: 28px; }

  .panel-black { background: var(--black); }
  .photo-resort {
    background: linear-gradient(180deg, var(--sky-top) 0%, var(--sky-mid) 50%, #dff1fb 56%, var(--sea) 66%, var(--sea-deep) 100%);
  }
  .photo-underwater {
    background: linear-gradient(180deg, #2fa8ec 0%, #0b7fd6 55%, #0a5fb0 100%);
  }
  .photo-atoll {
    background: radial-gradient(ellipse at 45% 40%, #6fa0a8 0%, #2b5264 30%, #0d1c2c 65%, #000 100%);
  }

  .flap { background: var(--black); }
  .cut-mark { position: absolute; font-size: 12px; font-weight: 700; color: var(--mark); }

  .office { position: absolute; color: var(--ink); font-weight: 700; }
  .office__title { font-size: 15px; line-height: 1.1; }
  .office__company { font-size: 10.5px; line-height: 1.2; }
  .office__line { font-size: 7px; line-height: 1.55; }

  .brand-box { position: absolute; background: var(--white); display: flex; align-items: center; justify-content: center; }
  .brand-box__name { font-size: 28px; font-weight: 700; color: var(--green); letter-spacing: 1px; }

  .brand-name { position: absolute; font-weight: 700; color: var(--cyan); line-height: 1; }
  .brand-tagline { position: absolute; font-weight: 400; color: var(--pink); letter-spacing: 1px; line-height: 1; }

  .upside-down { transform: rotate(180deg); transform-origin: center; }
</style>
</head>
<body>

  <!-- Front face -->
  <div class="label label--title" style="left:182px; top:0px;">front</div>
  <div class="label label--side" style="left:512px; top:186px;">up</div>
  <div class="label label--side" style="left:198px; top:936px;">down</div>

  <section class="front">
    <div class="abs panel-black" style="left:32px; top:100px; width:468px; height:362px;"></div>
    <div class="abs photo-atoll" role="img" aria-label="Aerial photo of a Maldives atoll at dusk" style="left:32px; top:260px; width:270px; height:202px;"></div>
    <div class="abs upside-down" style="left:32px; top:100px; width:468px; height:362px;">
      <div class="brand-name" style="left:96px; top:118px; font-size:70px;">Bluelark</div>
      <div class="brand-tagline" style="left:140px; top:212px; font-size:14px;">BLUELARK VOYAGE TRAVEL</div>
    </div>

    <div class="abs flap" style="left:0; top:588px; width:30px; height:230px;"></div>
    <div class="abs flap" style="left:498px; top:588px; width:30px; height:230px;"></div>
    <span class="cut-mark" style="left:10px; top:748px;">x</span>
    <span class="cut-mark" style="left:10px; top:795px;">x</span>
    <span class="cut-mark" style="left:508px; top:752px;">x</span>
    <span class="cut-mark" style="left:508px; top:795px;">x</span>

    <div class="abs photo-resort" role="img" aria-label="Maldives resort infinity pool with sun loungers, palm and water villas" style="left:32px; top:462px; width:468px; height:358px;"></div>

    <div class="office" style="left:105px; top:466px;">
      <div class="office__title">London Office :</div>
      <div class="office__company">Bluelark Voyage Ltd.</div>
      <div class="office__line">Ferncliff House, 48 Harbour Lane</div>
      <div class="office__line">London SE9 4QT</div>
      <div class="office__line">Tel : + 44 20 7000 1234</div>
      <div class="office__line">Fax : + 44 20 7000 5678</div>
      <div class="office__line">Email : info@bluelarkvoyage.example</div>
    </div>
    <div class="office" style="left:280px; top:562px;">
      <div class="office__title">Male Office :</div>
      <div class="office__company">Bluelark Voyage Ltd.</div>
      <div class="office__line">Ma. Coralreef Lane , Male</div>
      <div class="office__line">Maldives</div>
      <div class="office__line">Tel : + 960 300 1122</div>
      <div class="office__line">Fax : + 960 300 3344</div>
      <div class="office__line">Email : info@bluelarkvoyage.example</div>
    </div>

    <div class="brand-box" style="left:123px; top:747px; width:301px; height:68px;">
      <span class="brand-box__name">Bluelark</span>
    </div>

    <div class="abs photo-underwater" role="img" aria-label="Manta ray gliding through clear blue water" style="left:32px; top:820px; width:468px; height:112px;"></div>
  </section>

  <!-- Back face -->
  <div class="label label--side" style="left:660px; top:136px;">up</div>
  <div class="label label--side" style="left:623px; top:556px;">down</div>
  <div class="label label--title" style="left:865px; top:944px;">back</div>

  <section class="back">
    <div class="abs photo-resort" role="img" aria-label="Maldives resort infinity pool with sun loungers, palm and water villas" style="left:706px; top:106px; width:468px; height:361px;"></div>

    <div class="office" style="left:780px; top:112px;">
      <div class="office__title">London Office :</div>
      <div class="office__company">Bluelark Voyage Ltd.</div>
      <div class="office__line">Ferncliff House, 48 Harbour Lane</div>
      <div class="office__line">London SE9 4QT</div>
      <div class="office__line">Tel : + 44 20 7000 1234</div>
      <div class="office__line">Fax : + 44 20 7000 5678</div>
      <div class="office__line">Email : info@bluelarkvoyage.example</div>
    </div>
    <div class="office" style="left:955px; top:208px;">
      <div class="office__title">Male Office :</div>
      <div class="office__company">Bluelark Voyage Ltd.</div>
      <div class="office__line">Ma. Coralreef Lane , Male</div>
      <div class="office__line">Maldives</div>
      <div class="office__line">Tel : + 960 300 1122</div>
      <div class="office__line">Fax : + 960 300 3344</div>
      <div class="office__line">Email : info@bluelarkvoyage.example</div>
    </div>

    <div class="brand-box" style="left:798px; top:394px; width:301px; height:68px;">
      <span class="brand-box__name">Bluelark</span>
    </div>

    <div class="abs panel-black" style="left:706px; top:467px; width:468px; height:140px;"></div>
    <div class="abs panel-black" style="left:682px; top:600px; width:518px; height:228px;"></div>
    <div class="brand-name" style="left:812px; top:700px; font-size:76px;">Bluelark</div>
    <div class="brand-tagline" style="left:878px; top:786px; font-size:14px;">BLUELARK VOYAGE TRAVEL</div>

    <div class="abs photo-underwater" role="img" aria-label="Manta ray gliding through clear blue water" style="left:710px; top:830px; width:466px; height:108px;"></div>
    <span class="cut-mark" style="left:716px; top:836px;">x</span>
    <span class="cut-mark" style="left:1162px; top:844px;">x</span>
    <span class="cut-mark" style="left:716px; top:916px;">x</span>
    <span class="cut-mark" style="left:1162px; top:916px;">x</span>
  </section>

</body>
</html>
```